Business Website Re-design, Sharepoint, Office 365

Re-design of our existing Office 365 public website http://www.morrowvaltek.com. New site must use SharePoint and be compatible with Office 365 Hosting. A preliminary site layout and design is provided but creative suggestions and alternatives will be considered. Please see our attached power point presentation for details on the layout, and site design we are looking for.

Target Market(s)

Industrial Automation

Industry/Entity Type

Business

Coding

Coded - Design and coding required

Number of Pages Required

5+ page

Font styles to use
Serif
Sans Serif

Requirements
Must have
• SharePoint & Office 365 Compatible

```html
<!DOCTYPE html>
<html lang="en">
<head>
<meta charset="utf-8">
<title>Morrow Valtek Controls</title>
<link rel="stylesheet" href="https://fonts.googleapis.com/css2?family=Exo:wght@400;500;600&family=Open+Sans:wght@400;600&family=Oswald:wght@400&display=swap">
<style>
:root{
  --orange:#e8501c;
  --orange-light:#f26a30;
  --orange-dark:#d23f12;
  --ink:#222;
  --muted:#555;
  --dark:#141414;
  --darker:#0e0e0e;
  --line:#3a3a3a;
  --footer-text:#8a8a8a;
  --light:#f1f1f1;
  --white:#fff;
}
*{box-sizing:border-box;margin:0;padding:0}
html,body{width:1200px;height:2410px;overflow:hidden;background:var(--white)}
body{font-family:"Open Sans",Arial,sans-serif;color:var(--ink);position:relative}
.abs{position:absolute}
.heading{font-family:"Exo",Arial,sans-serif}

/* header */
.site-header{position:absolute;left:0;top:0;width:1200px;height:130px;background:var(--white)}
.brand{left:98px;top:48px;display:flex;align-items:center;gap:10px}
.brand-dot{width:26px;height:26px;border-radius:50%;background:var(--orange)}
.brand-name{font-family:"Exo",Arial,sans-serif;font-weight:600;font-size:26px;color:var(--orange);letter-spacing:1px}
.contact-top{left:850px;top:46px;display:flex;gap:18px;align-items:center}
.contact-top .lines{font-size:15px;line-height:26px}
.contact-top .mail{color:#444}
.contact-top .phone{color:var(--orange)}

/* nav */
.main-nav{position:absolute;left:0;top:130px;width:1200px;height:60px;background:linear-gradient(var(--orange-light),var(--orange-dark))}
.main-nav a{position:absolute;top:20px;color:var(--white);text-decoration:none;font-family:"Exo",Arial,sans-serif;font-size:16px}

/* hero */
.hero{position:absolute;left:0;top:190px;width:1200px;height:524px;background:linear-gradient(180deg,#3d3a3c 0%,#57504c 18%,#35363a 40%,#1f2226 70%,#16181b 100%)}
.hero-title{left:133px;top:222px;background:rgba(20,20,20,.85);padding:6px 14px;font-family:"Oswald",Arial,sans-serif;font-size:40px;color:var(--white);line-height:48px}
.hero-more{left:133px;top:284px;width:140px;height:34px;background:var(--orange);clip-path:polygon(0 0,100% 0,88% 100%,0 100%);color:var(--white);font-size:15px;padding:6px 14px}
.hero-arrow{top:254px;width:30px;height:30px;border-radius:50%;background:rgba(0,0,0,.35)}

/* welcome */
.welcome{position:absolute;left:0;top:714px;width:1200px;height:239px;text-align:center}
.welcome h1{font-family:"Exo",Arial,sans-serif;font-weight:500;font-size:34px;margin-top:36px;color:#1a1a1a}
.welcome p{width:780px;margin:16px auto 0;font-size:11.5px;line-height:21px;color:#333}
.btn{display:inline-block;background:var(--orange);color:var(--white);font-family:"Exo",Arial,sans-serif;font-size:14px;border-radius:3px}
.welcome .btn{margin-top:22px;width:194px;height:41px;line-height:41px}

/* services */
.services{position:absolute;left:0;top:953px;width:1200px;height:549px;background:linear-gradient(180deg,#2b1c12 0%,#3e2614 35%,#1b140f 75%,#0c0c0c 100%)}
.services h2{position:absolute;top:24px;width:100%;text-align:center;font-family:"Exo",Arial,sans-serif;font-weight:400;font-size:33px;color:var(--white)}
.services .sub{position:absolute;top:66px;width:100%;text-align:center;font-family:"Exo",Arial,sans-serif;font-size:15px;color:var(--white);letter-spacing:.5px}
.service-card{position:absolute;top:115px;width:232px}
.service-photo{height:159px}
.service-label{height:45px;background:var(--orange);color:var(--white);text-align:center;line-height:45px;font-family:"Exo",Arial,sans-serif;font-size:17px}
.service-list{height:149px;border:1px solid rgba(255,255,255,.12);border-top:0;background:rgba(0,0,0,.35);list-style:none;padding:20px 0 0 20px}
.service-list li{color:var(--white);font-family:"Exo",Arial,sans-serif;font-size:14px;height:28.5px;display:flex;align-items:center;gap:12px}
.bullet{width:11px;height:11px;border:2px solid var(--white);border-radius:50%;position:relative}
.bullet::after{content:"";position:absolute;left:2px;top:2px;width:3px;height:3px;background:var(--white);border-radius:50%}
.slider-dot{top:497px;width:22px;height:22px}

/* news */
.news{position:absolute;left:0;top:1502px;width:1200px;height:481px}
.section-title{font-family:"Exo",Arial,sans-serif;font-size:20px;color:#222}
.news-item{position:absolute;left:98px;width:660px;height:164px}
.news-photo{position:absolute;left:0;top:0;width:230px;height:164px}
.news-body{position:absolute;left:257px;top:0;width:400px}
.news-body h3{font-family:"Exo",Arial,sans-serif;font-weight:400;font-size:16px;color:#222}
.news-date{font-family:"Exo",Arial,sans-serif;font-size:15px;color:var(--orange);margin-top:12px}
.news-body p{font-size:11px;line-height:20.5px;color:#333;margin-top:6px}
.read-more{display:flex;align-items:center;gap:6px;font-family:"Exo",Arial,sans-serif;font-size:12px;margin-top:9px;color:#222}
.testimonial{position:absolute;left:834px;top:39px;width:266px;height:330px;background:#f6f6f6;border:1px solid #e6e6e6}
.testimonial h2{position:absolute;left:18px;top:16px}
.testimonial blockquote{position:absolute;left:40px;top:60px;width:206px;font-size:11px;line-height:20px;color:#555;text-align:justify}
.quote-mark{font-family:Georgia,serif;font-size:30px;color:#555}
.avatar{left:30px;top:194px;width:110px;height:110px;border-radius:50%;background:linear-gradient(#d9d2cc,#9c8d83);border:4px solid var(--white)}
.person{left:168px;top:236px;font-size:12px;line-height:21px;color:#222}
.person .role{color:#666}

/* partners */
.partners{position:absolute;left:0;top:1983px;width:1200px;height:87px;background:var(--light)}
.partner{top:26px;height:36px;background:#cfcfcf;border-radius:4px}

/* footer */
.site-footer{position:absolute;left:0;top:2070px;width:1200px;height:285px;background:linear-gradient(#1c1c1c,#121212)}
.footer-title{font-family:"Exo",Arial,sans-serif;font-size:17px;color:var(--white)}
.field{background:#0d0d0d;border:1px solid #222;color:#888;font-size:10px;padding:9px}
.send{left:100px;top:230px;width:83px;height:30px;line-height:30px;text-align:center;background:var(--orange);color:var(--white);font-family:"Exo",Arial,sans-serif;font-size:13px}
.info-row{left:448px;display:flex;font-size:12px;color:var(--footer-text)}
.info-row .label{width:135px;display:flex;gap:12px;align-items:center;font-family:"Exo",Arial,sans-serif;color:#9a9a9a}
.info-row .value{line-height:20px}
.expertise{left:862px;top:28px}
.expertise ul{list-style:none;margin-top:14px}
.expertise li{font-size:10.5px;color:#7a7a7a;height:20.6px;display:flex;align-items:center;gap:12px;padding-left:2px}
.bottom-bar{position:absolute;left:0;top:2355px;width:1200px;height:55px;background:var(--darker)}
.copyright{left:98px;top:21px;font-size:11px;color:#777}
.social{top:16px;width:23px;height:23px;border:1px solid #555;border-radius:50%}
</style>
</head>
<body>

<header class="site-header">
  <div class="abs brand"><span class="brand-dot"></span><span class="brand-name">MORROW VALTEK</span></div>
  <div class="abs contact-top">
    <svg width="26" height="34" viewBox="0 0 26 34"><path d="M6 2 L11 2 L13 10 L9 13 C10 19 13 23 17 25 L20 21 L25 24 L24 31 C14 33 3 20 2 7 Z" fill="#cfcfcf"/></svg>
    <div class="lines"><div class="mail">info@morrowvaltek.com</div><div class="phone">1.877.555.0148</div></div>
  </div>
</header>

<nav class="main-nav">
  <a style="left:98px">Home</a>
  <a style="left:198px">About Us</a>
  <a style="left:329px">Services</a>
  <a style="left:452px">Products</a>
  <a style="left:558px">Equipment</a>
  <a style="left:720px">News</a>
  <a style="left:820px">Remote Support</a>
  <a style="left:1006px">Contact Us</a>
</nav>

<section class="hero" role="img" aria-label="City skyline at dusk seen from above">
  <div class="abs hero-title">MORROW VALTEK CONTROLS</div>
  <div class="abs hero-more">View More</div>
  <svg class="abs hero-arrow" style="left:53px" viewBox="0 0 30 30"><path d="M18 8 L11 15 L18 22" stroke="#fff" stroke-width="3" fill="none"/></svg>
  <svg class="abs hero-arrow" style="left:1124px" viewBox="0 0 30 30"><path d="M12 8 L19 15 L12 22" stroke="#fff" stroke-width="3" fill="none"/></svg>
</section>

<section class="welcome">
  <h1>WELCOME TO OUR COMPANY!</h1>
  <p>Lorem ipsum dolor sit amet, consectetur adipisicing elit, sed do eiusmod tempor incididunt ut labore et dolore magna aliqua. Ut enim ad minim veniam, quis nostrud exercitation ullamco laboris nisi ut aliquip ex ea commodo consequat. Duis aute irure dolor in reprehenderit in voluptate velit esse cillum dolore eu fugiat. Lorem ipsum dolor sit amet, consectetur adipisicing elit, sed do eiusmod tempor</p>
  <span class="btn">MORE INFORMATIONS</span>
</section>

<section class="services" aria-label="Our Services">
  <h2>Our Services</h2>
  <div class="sub">instrumentation, Electrical, Manufacturing &amp; Design</div>

  <div class="service-card" style="left:98px">
    <div class="service-photo" role="img" aria-label="Two engineers in hard hats reviewing plans" style="background:linear-gradient(#8fb4d8,#c9a66a)"></div>
    <div class="service-label">Project Management</div>
    <ul class="service-list"><li><span class="bullet"></span>Procurement</li><li><span class="bullet"></span>Scheduling</li><li><span class="bullet"></span>Costing</li><li><span class="bullet"></span>Reporting</li></ul>
  </div>
  <div class="service-card" style="left:355px">
    <div class="service-photo" role="img" aria-label="Hands holding a tablet showing a control app" style="background:linear-gradient(#9a8a80,#3f4a58)"></div>
    <div class="service-label">Controls &amp; Automation</div>
    <ul class="service-list"><li><span class="bullet"></span>PLC/HMI Programming</li><li><span class="bullet"></span>DCS Configuration</li><li><span class="bullet"></span>SCADA/RTU Systems</li><li><span class="bullet"></span>Data Acquisition Systems</li></ul>
  </div>
  <div class="service-card" style="left:612px">
    <div class="service-photo" role="img" aria-label="Engineer in a white hard hat on site" style="background:linear-gradient(#e0a24a,#c7cdd6)"></div>
    <div class="service-label">Engineering Services</div>
    <ul class="service-list"><li><span class="bullet"></span>Preliminary</li><li><span class="bullet"></span>Design</li><li><span class="bullet"></span>Electrical</li><li><span class="bullet"></span>Instrumentation</li></ul>
  </div>
  <div class="service-card" style="left:869px">
    <div class="service-photo" role="img" aria-label="Worker among industrial pipework" style="background:linear-gradient(#b7c0c9,#5b6570)"></div>
    <div class="service-label">Industries</div>
    <ul class="service-list"><li><span class="bullet"></span>Oil &amp; Gas Pipelines</li><li><span class="bullet"></span>Drilling</li><li><span class="bullet"></span>Oil Batteries</li><li><span class="bullet"></span>Well Services</li></ul>
  </div>

  <svg class="abs slider-dot" style="left:573px" viewBox="0 0 22 22"><circle cx="11" cy="11" r="11" fill="#fff"/><path d="M13 6 L8 11 L13 16" stroke="#111" stroke-width="3" fill="none"/></svg>
  <svg class="abs slider-dot" style="left:604px" viewBox="0 0 22 22"><circle cx="11" cy="11" r="11" fill="#fff"/><path d="M9 6 L14 11 L9 16" stroke="#111" stroke-width="3" fill="none"/></svg>
</section>

<section class="news">
  <h2 class="abs section-title" style="left:98px;top:26px;font-weight:400">RECENT NEWS</h2>

  <article class="news-item" style="top:66px">
    <div class="news-photo" role="img" aria-label="Refinery silhouette at sunset" style="background:linear-gradient(#e99a3a,#6a3413 60%,#1e120b)"></div>
    <div class="news-body">
      <h3>Nulla at diam ornare, aliquam urna vel,</h3>
      <div class="news-date">05 - MARCH - 2015</div>
      <p>Nulla at diam ornare, aliquam urna vel, commodo urna. Nam id risus a est luctus consectetur quis eget libero. Suspendisse potenti. Pellentesque habitant morbi tristique senectus et netus et malesuada fames Nulla at diam ornare, aliquam urna vel, commodo urna.</p>
      <div class="read-more">READ MORE <svg width="11" height="11" viewBox="0 0 11 11"><circle cx="5.5" cy="5.5" r="5.5" fill="#222"/><path d="M4.5 3 L7 5.5 L4.5 8" stroke="#fff" stroke-width="1.5" fill="none"/></svg></div>
    </div>
  </article>

  <article class="news-item" style="top:264px">
    <div class="news-photo" role="img" aria-label="Oil pump jacks at sunset" style="background:linear-gradient(#d8842e,#b2521c 55%,#2a160c)"></div>
    <div class="news-body">
      <h3>Nulla at diam ornare, aliquam urna vel,</h3>
      <div class="news-date">05 - MARCH - 2015</div>
      <p>Nulla at diam ornare, aliquam urna vel, commodo urna. Nam id risus a est luctus consectetur quis eget libero. Suspendisse potenti. Pellentesque habitant morbi tristique senectus et netus et malesuada fames Nulla at diam ornare, aliquam urna vel, commodo urna.</p>
      <div class="read-more">READ MORE <svg width="11" height="11" viewBox="0 0 11 11"><circle cx="5.5" cy="5.5" r="5.5" fill="#222"/><path d="M4.5 3 L7 5.5 L4.5 8" stroke="#fff" stroke-width="1.5" fill="none"/></svg></div>
    </div>
  </article>

  <aside class="testimonial">
    <h2 class="section-title" style="position:absolute;left:18px;top:16px;font-weight:400">TESTIMONIALS</h2>
    <span class="abs quote-mark" style="left:18px;top:50px">&ldquo;</span>
    <blockquote>Lorem ipsum dolor sit amet, consectetur adipiscing elit, sed do eiusmod tempor incididunt ut labore et dolore magna aliqua. Ut enim ad minim veniam, quis nostrud exercitation ullamco laboris nisi ut aliquip</blockquote>
    <span class="abs quote-mark" style="left:234px;top:160px">&rdquo;</span>
    <div class="abs avatar" role="img" aria-label="Portrait of the reviewer"></div>
    <div class="abs person"><div>Evan Marsh.</div><div class="role">Creative Artist</div></div>
  </aside>
</section>

<section class="partners" aria-label="Partners">
  <div class="abs partner" style="left:188px;width:114px"></div>
  <div class="abs partner" style="left:364px;width:116px"></div>
  <div class="abs partner" style="left:542px;width:116px"></div>
  <div class="abs partner" style="left:719px;width:116px"></div>
  <div class="abs partner" style="left:896px;width:116px"></div>
</section>

<footer class="site-footer">
  <h2 class="abs footer-title" style="left:100px;top:22px;font-weight:400">GET IN TOUCH</h2>
  <div class="abs field" style="left:100px;top:60px;width:153px;height:35px">Name</div>
  <div class="abs field" style="left:262px;top:60px;width:156px;height:35px">Email</div>
  <div class="abs field" style="left:100px;top:102px;width:318px;height:113px">Message</div>
  <div class="abs send">SEND</div>

  <div class="abs info-row" style="top:64px">
    <span class="label"><svg width="13" height="17" viewBox="0 0 13 17"><path d="M6.5 0 C2.9 0 0 2.8 0 6.3 C0 11 6.5 17 6.5 17 S13 11 13 6.3 C13 2.8 10.1 0 6.5 0 Z" fill="#9a9a9a"/><circle cx="6.5" cy="6.3" r="2.4" fill="#1a1a1a"/></svg>ADDRESS</span>
    <span class="value">118 Ridgeline Drive<br>PO Box 4410</span>
  </div>
  <div class="abs info-row" style="top:124px">
    <span class="label"><svg width="14" height="14" viewBox="0 0 14 14"><path d="M2 0 L5 0 L6 4 L4 5.5 C5 8 6 9 8.5 10 L10 8 L14 9 L14 12 C8 14 0 6 2 0 Z" fill="#9a9a9a"/></svg>CALL US</span>
    <span class="value">Toll Free: 1.877.555.0148</span>
  </div>
  <div class="abs info-row" style="top:170px">
    <span class="label"><svg width="16" height="12" viewBox="0 0 16 12"><rect x="1" y="1" width="14" height="10" fill="none" stroke="#9a9a9a" stroke-width="1.5"/><path d="M1 1 L8 7 L15 1" stroke="#9a9a9a" stroke-width="1.5" fill="none"/></svg>E - MAIL</span>
    <span class="value">info@morrowvaltek.com</span>
  </div>

  <div class="abs expertise">
    <h2 class="footer-title" style="font-weight:400;font-size:15px">TECHNICAL EXPERTISE</h2>
    <ul>
      <li><span>&rsaquo;</span>Gas Turbine Controls</li>
      <li><span>&rsaquo;</span>Reciprocating Engine Control</li>
      <li><span>&rsaquo;</span>Flared Gas Power Generation</li>
      <li><span>&rsaquo;</span>Control System Retrofits and Replacement</li>
      <li><span>&rsaquo;</span>Satellite Communication</li>
      <li><span>&rsaquo;</span>SCADA</li>
      <li><span>&rsaquo;</span>Remote Monitoring</li>
    </ul>
  </div>
</footer>

<div class="bottom-bar">
  <div class="abs copyright">&copy;2014 - 2015 Morrow Valtek Controls. Rights Reserved.</div>
  <span class="abs social" style="left:958px"></span>
  <span class="abs social" style="left:985px"></span>
  <span class="abs social" style="left:1012px"></span>
  <span class="abs social" style="left:1039px"></span>
  <span class="abs social" style="left:1066px"></span>
</div>

</body>
</html>
```